Killer Webpage Design

I currently have a self-hosted webpage through wordpress at www.vantrelmedia.com - the content is complete and I'm happy with this but I need it designed (no coding) to complete my requirements. I'm happy to take designs which are non-Wordpress if there is specific advantage in this.

My full branding logos are attached along with color files. My main aim is consistent branding across all areas (social media, business cards, emails, websites). I have the rest running but am not happy with the available default selections from Wordpress.

I would prefer to use the darker blue version of the logo as I feel this has more standout in online media, however I would appreciate submissions with both variants to help me choose.

With the homepage I will also want to see blog pages and category pages designed but this can come after I have selected a design to go with,

Sites that I like and are related to my business include the following:
http://www.plumora.com/au/accounting-software/
http://www.taskgriddle.com/home.aspx
https://brimtill.com/register
Updates

Apologies for the confusion - to clarify for designers I am looking for design only, no coding.

FYI - i have now uploaded business cards for an idea of the contemporary style of design completed so far.

Target Market(s)

small to medium business. Not systemised but looking for help and support.

Industry/Entity Type

Business

Requirements
Must have
• I'm looking for a minimalist professional page, with the ability to easily add new sections when required. I will also need a CMS to add blog posts on the go, with the same features that it currently has (comments, social logon etc)

```html
<!DOCTYPE html>
<html lang="en">
<head>
<meta charset="utf-8">
<title>Vantrel Media</title>
<link href="https://fonts.googleapis.com/css2?family=Roboto+Condensed:wght@400;700&family=Roboto:wght@400;500&display=swap" rel="stylesheet">
<style>
:root{
  --brand:#1d8fb0;
  --brand-light:#36c3e0;
  --navy:#1f5a78;
  --hero-top:#2a86a8;
  --hero-bottom:#1b5f7e;
  --text:#6b6b6b;
  --line:#e1e1e1;
  --footer:#1f5a78;
  --white:#ffffff;
}
*{box-sizing:border-box;margin:0;padding:0}
html,body{width:1180px;height:1200px;overflow:hidden;background:var(--white)}
body{font-family:"Roboto",Arial,sans-serif;color:var(--text);position:relative}
.wrap{position:absolute;left:117px;width:944px}

.site-header{position:absolute;top:0;left:0;width:1180px;height:90px;background:#f8f8f8;border-bottom:1px solid #e6e6e6}
.brand{position:absolute;left:117px;top:28px;display:flex;align-items:center;gap:10px;font-family:"Roboto Condensed",sans-serif;font-weight:700;font-size:28px;color:var(--brand)}
.brand-dot{width:30px;height:30px;border-radius:50%;background:var(--brand)}
.main-nav{position:absolute;right:117px;top:39px;display:flex;gap:24px;font-family:"Roboto Condensed",sans-serif;font-size:14.5px}
.main-nav a{color:var(--navy);text-decoration:none}

.hero{position:absolute;top:90px;left:0;width:1180px;height:452px;background:radial-gradient(ellipse at 40% 20%,var(--hero-top),var(--hero-bottom))}
.hero-title{position:absolute;left:116px;top:138px;font-family:"Roboto Condensed",sans-serif;font-weight:400;font-size:36px;color:var(--brand-light);letter-spacing:.5px}
.hero-text{position:absolute;left:118px;top:196px;width:420px;font-family:"Roboto Condensed",sans-serif;font-size:14.3px;line-height:22px;color:var(--white);text-transform:uppercase}
.btn-cart{position:absolute;left:118px;top:299px;padding:8px 10px;background:#2aa7c2;color:var(--white);font-family:"Roboto Condensed",sans-serif;font-size:12.5px;border:1px solid #5cc8dc}
.dots{position:absolute;left:117px;top:360px;display:flex;gap:8px}
.dots span{width:8px;height:8px;border-radius:50%;background:#d6dde1;border:1px solid #6c8a99}
.dots span.active{background:var(--white)}
.devices{position:absolute;left:548px;top:58px;width:516px;height:380px;border-radius:14px;background:linear-gradient(160deg,#d9dfe3,#9aa8b0 60%,#2a2f33)}

.features{position:absolute;top:575px;left:117px;width:944px;display:flex}
.feature{width:312px;text-align:center;border-right:1px solid var(--line);height:270px}
.feature:nth-child(2){width:322px;padding:0 14px}
.feature:first-child{padding-right:14px}
.feature:last-child{border-right:none;padding-left:14px;width:310px}
.feature-icon{width:86px;height:86px;margin:0 auto;border-radius:50%;border:1px solid #dcdcdc;background:#f4f4f4;display:flex;align-items:center;justify-content:center}
.feature-icon i{width:60px;height:60px;border-radius:50%;display:block}
.feature h2{margin-top:18px;font-family:"Roboto Condensed",sans-serif;font-weight:400;font-size:19px;color:var(--brand);text-transform:uppercase}
.feature p{margin-top:10px;font-size:12.2px;line-height:18px;text-align:justify;text-align-last:center}
.btn-more{display:inline-block;margin-top:20px;padding:6px 11px;background:var(--navy);color:var(--white);font-family:"Roboto Condensed",sans-serif;font-size:15.5px;border:1px solid #133d52;white-space:nowrap}

.partners{top:879px}
.partners-head{height:42px;border-top:1px solid var(--line);border-bottom:1px solid var(--line);display:flex;align-items:center;justify-content:space-between}
.partners-head h2{padding-left:4px;font-family:"Roboto",sans-serif;font-weight:500;font-size:18px;color:var(--navy)}
.arrows{display:flex;height:34px;border:1px solid var(--line)}
.arrows span{width:33px;display:flex;align-items:center;justify-content:center;color:#aaa;font-size:16px}
.arrows span+span{border-left:1px solid var(--line)}
.partner-list{display:flex;justify-content:space-between;align-items:center;margin-top:40px;padding:0 14px}
.partner{display:flex;align-items:center;gap:10px;font-family:"Roboto",sans-serif;font-weight:500;font-size:30px;color:#333;white-space:nowrap}
.partner i{width:34px;height:34px;border-radius:50%;background:#555;display:block}

.newsletter{position:absolute;left:117px;top:1053px;width:630px;height:71px;border:1px solid var(--line);display:flex;align-items:center;padding:0 12px;gap:8px}
.newsletter label{font-family:"Roboto Condensed",sans-serif;font-size:16px;color:var(--navy);white-space:nowrap}
.newsletter .field{width:340px;height:40px;border:1px solid #d6d6d6}
.btn-signup{margin-left:4px;padding:8px 8px;background:var(--navy);color:var(--white);font-family:"Roboto",sans-serif;font-weight:500;font-size:14px;border:1px solid #133d52;white-space:nowrap}
.social{position:absolute;left:756px;top:1053px;width:310px;height:71px;border:1px solid var(--line);display:flex;align-items:center;justify-content:center;gap:18px}
.social span{width:32px;height:32px;display:block}

.site-footer{position:absolute;left:0;top:1154px;width:1180px;height:46px;background:var(--footer);color:var(--white);font-size:12.8px}
.footer-links{position:absolute;left:117px;top:15px}
.footer-links a{color:var(--white);text-decoration:none}
.copyright{position:absolute;right:119px;top:15px}
</style>
</head>
<body>
<header class="site-header">
  <div class="brand"><span class="brand-dot"></span>Vantrel Media</div>
  <nav class="main-nav">
    <a href="#">Software Training &amp; Implementation</a>
    <a href="#">Project Management</a>
    <a href="#">Business Process Analysis</a>
    <a href="#">Blog</a>
    <a href="#">About</a>
    <a href="#">Contact</a>
  </nav>
</header>

<section class="hero">
  <h1 class="hero-title">VANTREL MEDIA</h1>
  <p class="hero-text">Run your business and access your accounts from work, home or on the go.invite others to view your accounts and provide valuable real-time advice.your data is completely secure even if your computer is lost or stolen.</p>
  <span class="btn-cart">ADD TO CART</span>
  <div class="dots"><span></span><span class="active"></span><span></span><span></span></div>
  <div class="devices" role="img" aria-label="Laptop and smartphone showing an online accounting dashboard"></div>
</section>

<section class="features">
  <article class="feature">
    <div class="feature-icon"><i role="img" aria-label="Cloud icon" style="background:radial-gradient(circle at 40% 35%,#5bb8f0,#1c6fc2)"></i></div>
    <h2>Training &amp; Implementation</h2>
    <p>Importer is a flagship solution build to import large amount of data into Customer Service Software like Helpnest and Internal Bug tracking systems like Bugrally from legacy systems,Flat file,Datavault,Orvix DB and numerous other systems.</p>
    <span class="btn-more">LEAR MORE</span>
  </article>
  <article class="feature">
    <div class="feature-icon"><i role="img" aria-label="Team icon" style="background:radial-gradient(circle at 40% 50%,#f4a640,#b9c2cc)"></i></div>
    <h2>Project Management</h2>
    <p>Importer is a flagship solution build to import large amount of data into Customer Service Software like Helpnest and Internal Bug tracking systems like Bugrally from legacy systems,Flat file,Datavault,Orvix DB and numerous other systems.</p>
    <span class="btn-more">LEAR MORE</span>
  </article>
  <article class="feature">
    <div class="feature-icon"><i role="img" aria-label="Gear icon" style="background:radial-gradient(circle,#e8f2f8 20%,#2b7fc0 40%,#9aa4ad 70%)"></i></div>
    <h2>Process Analysis</h2>
    <p>Importer is a flagship solution build to import large amount of data into Customer Service Software like Helpnest and Internal Bug tracking systems like Bugrally from legacy systems,Flat file,Datavault,Orvix DB and numerous other systems.</p>
    <span class="btn-more">LEAR MORE</span>
  </article>
</section>

<section class="wrap partners">
  <div class="partners-head">
    <h2>OUR PARTNER PROGRAM</h2>
    <div class="arrows"><span>&#8249;</span><span>&#8250;</span></div>
  </div>
  <div class="partner-list">
    <div class="partner"><i></i>Ledgerwise</div>
    <div class="partner">Opalsys</div>
    <div class="partner"><i></i>Ripple Books</div>
    <div class="partner"><i></i>Corvanta</div>
  </div>
</section>

<form class="newsletter">
  <label>SIGN UP OUR NEWSLETTER</label>
  <span class="field"></span>
  <span class="btn-signup">SIGN UP</span>
</form>
<div class="social">
  <span role="img" aria-label="Social profile link" style="background:#3a5a9a"></span>
  <span role="img" aria-label="Social profile link" style="background:#22b8ea"></span>
  <span role="img" aria-label="Social profile link" style="background:#d9262d"></span>
  <span role="img" aria-label="Social profile link" style="background:#c8231d"></span>
  <span role="img" aria-label="Social profile link" style="background:#dc4a38"></span>
</div>

<footer class="site-footer">
  <div class="footer-links"><a href="#">About us</a> &nbsp;|&nbsp; <a href="#">Careers</a> &nbsp;|&nbsp; <a href="#">Media</a> &nbsp;|&nbsp; <a href="#">Blog</a> &nbsp;|&nbsp; <a href="#">Privacy Policy</a> &nbsp;|&nbsp; <a href="#">TErms of use</a></div>
  <div class="copyright">© 2013 Vantrel Media</div>
</footer>
</body>
</html>
```